Real Estate Company
Residential & Commercial
Sales & Property Management

would like to use the logo i uploaded but would really love a black back ground...I think with the gold fleur dis lis and the maroon lettering it would really look great!

Industry/Entity Type

Business

Contact Information for Business Card

Bright Harbor Real Estate Co.
Renata Dubois
Broker/Owner
337-502-4173 Cell
337-618-9034 Office
4172 Pelton Rd Maurice LA 70555

```html
<!DOCTYPE html>
<html lang="en">
<head>
<meta charset="utf-8">
<title>Bright Harbor Real Estate Co. – Business Card</title>
<link rel="stylesheet" href="https://fonts.googleapis.com/css2?family=Roboto+Condensed:wght@300;400;700&display=swap">
<style>
  :root {
    --page: #ffffff;
    --card-edge: #231f20;
    --card-glow: #4d4c4f;
    --maroon: #b3202a;
    --gold: #f3dea0;
    --cream: #fbf0c8;
    --ink-light: #ffffff;
  }
  * { margin: 0; padding: 0; box-sizing: border-box; }
  html, body {
    width: 1200px;
    height: 960px;
    overflow: hidden;
    background: var(--page);
  }
  .canvas {
    position: relative;
    width: 1200px;
    height: 960px;
  }
  .business-card {
    position: absolute;
    left: 178px;
    top: 242px;
    width: 839px;
    height: 478px;
    background: radial-gradient(ellipse 60% 75% at 48% 52%, var(--card-glow) 0%, #3a393b 45%, var(--card-edge) 100%);
    font-family: "Roboto Condensed", "Arial Narrow", sans-serif;
  }
  .frame-outer {
    position: absolute;
    left: 29px;
    top: 29px;
    width: 780px;
    height: 419px;
    border: 6px solid var(--maroon);
  }
  .frame-inner {
    position: absolute;
    inset: 0;
    border: 9px solid var(--gold);
  }
  .brand {
    position: absolute;
    left: 78px;
    top: 90px;
    display: flex;
    align-items: center;
    gap: 18px;
    color: var(--cream);
    font-weight: 700;
  }
  .brand-dot {
    width: 46px;
    height: 46px;
    border-radius: 50%;
    background: var(--maroon);
    flex: none;
  }
  .brand-name {
    font-size: 54px;
    line-height: 1.02;
    letter-spacing: -0.5px;
  }
  .contact {
    position: absolute;
    right: 73px;
    top: 308px;
    text-align: right;
    color: var(--ink-light);
    font-weight: 300;
    font-size: 27.5px;
    line-height: 36px;
  }
  .contact-name { font-weight: 700; }
  .contact-title { font-weight: 400; }
</style>
</head>
<body>
<main class="canvas">
  <section class="business-card" aria-label="Bright Harbor Real Estate Co. business card">
    <div class="frame-outer"><div class="frame-inner"></div></div>

    <div class="brand">
      <span class="brand-dot" aria-hidden="true"></span>
      <h1 class="brand-name">Bright Harbor<br>Real Estate Co.</h1>
    </div>

    <address class="contact" style="font-style: normal;">
      <p><span class="contact-name">Renata Dubois,</span> <span class="contact-title">Broker/Owner</span></p>
      <p>337.502.4173 Cell &bull; 337.618.9034 Office</p>
      <p>4172 Pelton Rd., Maurice LA 70555</p>
    </address>
  </section>
</main>
</body>
</html>
```